Corvel Lane

Small ageny public transit advocacy, funding and compliance.
Consulting and lobbying efforts for small public transit agencies and communities exploring public transit opportunities.
Updates

I was interested in a simple line sketch suggesting motion, mobility. The card will be black on white. I would like it to include the bUs ones brief; Advocacy, Funding , and Compliance for small transit agencies.

Reason: I have been traveling and have had limited time to respond. Thank you all for your submit talks.

Industry/Entity Type

Consulting

Contact Information for Business Card

Mark D Loyer
Phone (614) 380-2917
Email markdloyer@vantomail.test

```html
<!DOCTYPE html>
<html lang="en">
<head>
<meta charset="utf-8">
<title>Corvel Lane — Business Card</title>
<link rel="stylesheet" href="https://fonts.googleapis.com/css2?family=Montserrat:wght@500;800&family=Open+Sans:wght@400&display=swap">
<style>
  :root {
    --backdrop: #e6e6e6;
    --card-black: #050505;
    --accent-green: #86c21a;
    --text-white: #ffffff;
    --text-soft: #f0f0f0;
  }
  * { box-sizing: border-box; margin: 0; padding: 0; }
  html, body {
    width: 1200px;
    height: 787px;
    overflow: hidden;
    background: var(--backdrop);
  }
  .card-sheet {
    position: absolute;
    left: 25px;
    top: 233px;
    display: flex;
    gap: 30px;
  }
  .business-card {
    position: relative;
    width: 560px;
    height: 320px;
    background: var(--card-black);
    overflow: hidden;
  }

  /* Front */
  .edge-stripe {
    position: absolute;
    left: 0; top: 0;
    width: 15px; height: 100%;
    background: var(--accent-green);
  }
  .brand {
    display: flex;
    align-items: center;
    gap: 10px;
  }
  .brand-mark {
    width: 20px; height: 20px;
    background: var(--accent-green);
    flex: none;
  }
  .brand-name {
    font-family: "Montserrat", sans-serif;
    font-weight: 800;
    font-size: 23px;
    letter-spacing: 0.3px;
    color: var(--text-white);
    text-transform: uppercase;
    line-height: 1;
    white-space: nowrap;
  }
  .card-front .brand {
    position: absolute;
    left: 46px;
    top: 30px;
  }
  .person-name {
    position: absolute;
    left: 60px;
    top: 104px;
    font-family: "Open Sans", sans-serif;
    font-weight: 400;
    font-size: 26px;
    color: var(--accent-green);
    white-space: nowrap;
  }
  .contact-list {
    position: absolute;
    left: 60px;
    top: 160px;
    list-style: none;
    font-family: "Open Sans", sans-serif;
    font-size: 15px;
    color: var(--text-soft);
  }
  .contact-item {
    display: flex;
    align-items: center;
    gap: 12px;
    height: 28px;
    white-space: nowrap;
  }
  .contact-icon { width: 18px; height: 15px; fill: var(--accent-green); flex: none; }
  .vehicle-graphic {
    position: absolute;
    right: 0;
    top: 12px;
    width: 168px;
    height: 308px;
    background: linear-gradient(180deg, #8cc824 0%, var(--accent-green) 100%);
    border-top-left-radius: 28px;
  }
  .service-list {
    position: absolute;
    right: 16px;
    top: 56px;
    list-style: none;
    font-family: "Montserrat", sans-serif;
    font-weight: 500;
    font-size: 13px;
    color: var(--card-black);
    line-height: 1.6;
    white-space: nowrap;
  }
  .service-item::before {
    content: "";
    display: inline-block;
    width: 5px; height: 5px;
    border-radius: 50%;
    background: var(--card-black);
    margin-right: 5px;
    vertical-align: middle;
  }

  /* Back */
  .card-back .brand {
    position: absolute;
    left: 50%;
    top: 50%;
    transform: translate(-50%, -50%);
    gap: 14px;
  }
  .card-back .brand-mark { width: 30px; height: 30px; }
  .card-back .brand-name { font-size: 36px; }
  .base-stripe {
    position: absolute;
    left: 0; bottom: 0;
    width: 100%; height: 12px;
    background: var(--accent-green);
  }
</style>
</head>
<body>
  <div class="card-sheet">
    <main class="business-card card-front">
      <div class="edge-stripe"></div>

      <header class="brand">
        <span class="brand-mark"></span>
        <span class="brand-name">Corvel Lane</span>
      </header>

      <h1 class="person-name">Mark D Loyer</h1>

      <ul class="contact-list">
        <li class="contact-item">
          <svg class="contact-icon" viewBox="0 0 30 24" aria-hidden="true">
            <path d="M7 2c1 0 2 .5 2.5 1.5l2 4c.4 1 .2 2-.6 2.7l-1.6 1.3c1.2 2.6 3.2 4.6 5.8 5.8l1.3-1.6c.7-.8 1.7-1 2.7-.6l4 2c1 .5 1.5 1.5 1.5 2.5 0 2.4-2 4.4-4.4 4.4C11 24 2 15 2 6.4 2 4 4 2 6.4 2z"/>
          </svg>
          <span class="contact-text">(614) 380-2917</span>
        </li>
        <li class="contact-item">
          <svg class="contact-icon" viewBox="0 0 30 24" aria-hidden="true">
            <path d="M2 3h26v2L15 14 2 5z"/>
            <path d="M2 8l13 9 13-9v13H2z"/>
          </svg>
          <span class="contact-text">markdloyer@vantomail.test</span>
        </li>
      </ul>

      <div class="vehicle-graphic" role="img" aria-label="Large front view of a transit bus in green"></div>

      <ul class="service-list">
        <li class="service-item">Advocacy</li>
        <li class="service-item">Funding</li>
        <li class="service-item">Compliance</li>
      </ul>
    </main>

    <section class="business-card card-back">
      <div class="brand">
        <span class="brand-mark"></span>
        <span class="brand-name">Corvel Lane</span>
      </div>
      <div class="base-stripe"></div>
    </section>
  </div>
</body>
</html>
```